Weight Loss Challenge Social Media Graphics

Create 6-7 individual social media graphics (square size) to encourage folks to join our weight loss challenge. For the color scheme of the graphics, use the color palette attached

Note: each graphic can contain any of the stock photography attached or just the single picture of me (brown shirt) but a few should be ONLY the text
For some graphics we can say: JOIN US!
For some graphics, use only TEXT based

Target Market(s)

primarily women who want to get healthy

Industry/Entity Type

health and weight loss

Requirements
Must have
• The largest text should be: Ninety Days Bold

```html
<!DOCTYPE html>
<html lang="en">
<head>
<meta charset="utf-8">
<title>Ninety Days Bold – Challenge Graphic</title>
<link rel="stylesheet" href="https://fonts.googleapis.com/css2?family=Playfair+Display:ital,wght@1,500;1,600&family=Montserrat:wght@500&display=swap">
<style>
  :root {
    --rose: #c49e94;
    --cream: #f5e2d2;
    --banner: #f3dfd0;
    --banner-text: #b08a80;
    --photo-light: #ece3d6;
    --photo-mid: #cdb49f;
    --photo-deep: #a27a5c;
  }
  html, body {
    margin: 0;
    padding: 0;
    width: 1200px;
    height: 1200px;
    overflow: hidden;
    background: var(--rose);
  }
  .graphic {
    position: relative;
    width: 1200px;
    height: 1200px;
    background: var(--rose);
    overflow: hidden;
  }
  .headline {
    position: absolute;
    left: 63px;
    top: 150px;
    margin: 0;
    font-family: "Playfair Display", serif;
    font-style: italic;
    font-weight: 500;
    font-size: 102px;
    line-height: 1.06;
    color: var(--cream);
    letter-spacing: 1px;
  }
  .tagline {
    position: absolute;
    left: 63px;
    top: 480px;
    margin: 0;
    font-family: "Montserrat", sans-serif;
    font-weight: 500;
    font-size: 29px;
    line-height: 1.4;
    color: var(--cream);
  }
  .start-banner {
    position: absolute;
    left: 0;
    top: 766px;
    width: 592px;
    height: 106px;
  }
  .start-banner__text {
    position: absolute;
    left: 61px;
    top: 766px;
    height: 106px;
    line-height: 106px;
    margin: 0;
    font-family: "Montserrat", sans-serif;
    font-weight: 500;
    font-size: 30px;
    color: var(--banner-text);
    letter-spacing: 0.3px;
  }
  .portrait {
    position: absolute;
    left: 514px;
    top: 222px;
    width: 624px;
    height: 978px;
  }
  .dots {
    position: absolute;
    width: 78px;
    height: 30px;
  }
  .dots--top { left: 1059px; top: 66px; }
  .dots--bottom { left: 63px; top: 1102px; }
</style>
</head>
<body>
<main class="graphic">
  <h1 class="headline">Ninety Days<br>Bold</h1>
  <p class="tagline">Lose Up to 20 Pounds<br>in 6 Weeks!</p>

  <svg class="start-banner" viewBox="0 0 592 106" aria-hidden="true">
    <polygon points="0,0 592,0 530,106 0,106" fill="var(--banner)"/>
  </svg>
  <p class="start-banner__text">Begins Monday, Jan 6th</p>

  <svg class="portrait" viewBox="0 0 624 978" role="img" aria-label="Photo of the smiling coach in a camel turtleneck and black high-waisted jeans, standing against a light stone wall">
    <defs>
      <linearGradient id="portrait-tone" x1="0" y1="0" x2="0" y2="1">
        <stop offset="0" stop-color="var(--photo-light)"/>
        <stop offset="0.55" stop-color="var(--photo-mid)"/>
        <stop offset="1" stop-color="var(--photo-deep)"/>
      </linearGradient>
    </defs>
    <path d="M0,312 A312,312 0 0 1 624,312 L624,978 L0,978 Z" fill="url(#portrait-tone)"/>
  </svg>

  <svg class="dots dots--top" viewBox="0 0 78 30" aria-hidden="true">
    <g fill="var(--cream)">
      <circle cx="4" cy="4" r="3.6"/><circle cx="27" cy="4" r="3.6"/><circle cx="51" cy="4" r="3.6"/><circle cx="74" cy="4" r="3.6"/>
      <circle cx="4" cy="26" r="3.6"/><circle cx="27" cy="26" r="3.6"/><circle cx="51" cy="26" r="3.6"/><circle cx="74" cy="26" r="3.6"/>
    </g>
  </svg>
  <svg class="dots dots--bottom" viewBox="0 0 78 30" aria-hidden="true">
    <g fill="var(--cream)">
      <circle cx="4" cy="4" r="3.6"/><circle cx="27" cy="4" r="3.6"/><circle cx="51" cy="4" r="3.6"/><circle cx="74" cy="4" r="3.6"/>
      <circle cx="4" cy="26" r="3.6"/><circle cx="27" cy="26" r="3.6"/><circle cx="51" cy="26" r="3.6"/><circle cx="74" cy="26" r="3.6"/>
    </g>
  </svg>
</main>
</body>
</html>
```